Aviation Maintenance & Aircraft Cleaning Website

We need a fairly simple modern sleek website . Our company does aviation maintenance , aircraft cleaning , maintenance tracking . We work on KT420 HELICOPTERS , BELVANKO T82 HELICOPTERS , MORVELL TARRANT 512 HELICOPTERS. We would like a website that can be mobile as well with future ideas that an app where you could book cleanings and maintenance . Right now the biggest thing is for our customer to see a website , be able to book our services online and see our staff . the website must be modern and clean .

Target Market(s)

Aviation maintenance , aviation cleaning ,

Logo Text

TW but 1 image unlike the one i uploaded which is two . Im open for different aviation designs

Number of Pages Required

5+ page

Font styles to use
Serif

Requirements
Must have
• Home page , Aircraft Maintenance , Aircraft Cleaning , About Us , Contact , Careers

TW Aviation is insured and all of our mechanics are licensed by the NQB with an Airframe & Powerplant rating. ( FRONT PAGE )

Home page should have a simple nice picture of a KT420 or Belvanko T82 . My Logo as you can see seems like two logos . i would like 1 logo and made of the two if possible . (New ideas are welcome . )

Book a Cleaning Calendar should in the aircraft cleaning page . The aircraft cleaning page should have a picture of cleaning a helicopter or private jet .

Aircraft maintenance page should have a mechanic working on a helicopter . The Page should have a fast way to contact us .

We are a mobile AOG team who is available 24/7 . What we do
Scheduled & Unscheduled aircraft maintenance
Major & Minor repairs
STC installations
Aircraft Weight & Balance
Aircraft Painting
Aircraft Cleaning
Maintenance Tracking Utilizing Tracking Programs or spreadsheets
Removal & Installation of Components
Aircraft Pre Buy Inspections
Nice to have
• modern , sleek , aviation

Meet the Staff

Picture with Headset on flying in a helicopter

CEO Mateus Ferreira

Mateus Has been an aircraft mechanic for over 10 years . He has worked for the largest sightseeing & charter tourism company in the New York City area as well as repair stations & manufacturers. He has aircraft specific training to the Kestrane KT420 & Vornel 2K4. He has worked on several airframes including the Belvanko T82 and the Morvell 512. He has held every position in an aircraft maintenance department from mechanic up to Director of Maintenance . His work ethic and ability to manage mechanics in a organized and structured way gives any department or inspection a clear direction .

About Us

TW Aviation Services is company with aircraft maintenance experience . We focus on inspections of aircraft . Our Aircraft Mechanics who are pilots and IA's have experience many aircraft but specialize in the Kestrane KT420 , KT425 , KT435 . The Belvanko T82 and Morvell Tarrant 512 . Our focus is safety and to maintain aircraft day in and day out so our customer can operate the aircraft safely while keeping up with all the manufacturers inspections .

We know aircraft maintenance & maintenance planning . Leave the technical and tedious things to us . Get in your aircraft and fly knowing you have the best maintenance crew in the business.

```html
<!DOCTYPE html>
<html lang="en">
<head>
<meta charset="utf-8">
<title>TW Aviation — Aircraft Maintenance &amp; Cleaning</title>
<link rel="stylesheet" href="https://fonts.googleapis.com/css2?family=Josefin+Sans:wght@400;600;700&family=Noto+Serif:wght@400;700&display=swap">
<style>
:root{
  --blue:#1f45aa;
  --blue-dark:#183a93;
  --ink:#222630;
  --muted:#555a66;
  --line:#e2e4e9;
  --field:#f7f7f8;
  --pale:#f2f3f6;
  --white:#ffffff;
  --footer-bar:#4b4d52;
}
*{box-sizing:border-box;margin:0;padding:0}
html,body{width:1200px;height:4298px;overflow:hidden}
body{position:relative;background:var(--white);color:var(--ink);font-family:"Noto Serif",serif;font-size:12px}
.sans{font-family:"Josefin Sans",sans-serif}
.abs{position:absolute}
a{color:inherit;text-decoration:none}

/* top bar */
.topbar{top:0;left:0;width:1200px;height:40px;background:var(--blue);color:#fff;font-family:"Josefin Sans",sans-serif;font-size:11px}
.topbar .contact{position:absolute;right:162px;top:14px;display:flex;gap:24px;align-items:center}
.topbar .contact span{display:flex;gap:7px;align-items:center}

/* nav */
.nav{top:40px;left:0;width:1200px;height:85px;background:#f6f6f7}
.brand{display:flex;align-items:center;gap:8px;font-family:"Josefin Sans",sans-serif;font-weight:700;color:var(--blue);white-space:nowrap}
.nav .brand{position:absolute;left:160px;top:22px;font-size:26px}
.brand .dot{width:40px;height:40px;border-radius:50%;border:3px solid var(--blue);flex-shrink:0}
.menu{position:absolute;right:162px;top:37px;display:flex;gap:29px;font-family:"Josefin Sans",sans-serif;font-size:12px;color:#333;text-transform:uppercase}
.menu .active{color:var(--blue);border-bottom:1px solid var(--blue);padding-bottom:2px}

/* hero */
.hero{top:125px;left:0;width:1200px;height:751px;background:linear-gradient(180deg,#4f545c 0%,#8d929a 40%,#b5b8bd 65%,#3e4148 100%)}
.hero .shade{position:absolute;inset:0;background:rgba(20,24,34,.28)}
.hero-text{position:absolute;top:200px;left:0;width:1200px;text-align:center;color:#fff}
.eyebrow-light{font-family:"Josefin Sans",sans-serif;font-size:11px;letter-spacing:2px;text-transform:uppercase}
.hero h1{font-family:"Josefin Sans",sans-serif;font-weight:700;font-size:39px;line-height:48px;margin-top:16px}
.btn{display:inline-flex;align-items:center;justify-content:center;background:var(--blue);color:#fff;font-family:"Josefin Sans",sans-serif;font-weight:700;font-size:11px;text-transform:uppercase;letter-spacing:.5px}
.hero .btn{position:absolute;left:546px;top:402px;width:132px;height:46px}

/* booking */
.booking{top:781px;left:162px;width:876px;height:195px;background:#fff;box-shadow:0 6px 20px rgba(0,0,0,.08)}
.booking .label{position:absolute;left:0;top:0;width:277px;height:195px;background:var(--blue);color:#fff;text-align:center;padding-top:73px}
.booking .label small{font-family:"Josefin Sans",sans-serif;font-size:11px;text-transform:uppercase;display:block}
.booking .label strong{font-family:"Josefin Sans",sans-serif;font-size:32px;font-weight:700;display:block;margin-top:6px}
.field{position:absolute;width:168px;height:44px;background:var(--field);border:1px solid var(--line);font-family:"Josefin Sans",sans-serif;font-size:11px;color:#555;padding:15px 14px 0}
.submit{position:absolute;width:168px;height:43px;background:#757a82;color:#fff;font-family:"Josefin Sans",sans-serif;font-weight:700;font-size:10px;text-transform:uppercase;display:flex;align-items:center;justify-content:center}

/* shared headings */
.eyebrow{font-family:"Josefin Sans",sans-serif;font-size:10px;text-transform:uppercase;color:#555}
.title{font-family:"Josefin Sans",sans-serif;font-weight:700;font-size:31px;color:var(--ink)}
.body{font-size:11.5px;line-height:22.5px;color:#3c404a}

/* about */
.about-media{top:1060px;left:157px;width:400px;height:445px;border:1px solid #ccc;background:linear-gradient(135deg,#6b6f77,#aeb2b8 55%,#d9dbde)}
.play{position:absolute;left:168px;top:190px;width:66px;height:66px;border-radius:50%;background:rgba(255,255,255,.85);display:flex;align-items:center;justify-content:center}
.quote{top:1228px;left:611px;width:427px;height:80px;background:var(--pale);color:var(--blue);font-family:"Josefin Sans",sans-serif;font-size:13px;line-height:22px;padding:17px 18px;text-transform:uppercase}
.divider{height:1px;background:var(--line)}
.ceo{top:1460px;left:609px;display:flex;align-items:center;gap:12px}
.avatar{width:50px;height:50px;border-radius:50%;background:linear-gradient(135deg,#3a3f48,#9aa0a8)}
.ceo b{font-family:"Josefin Sans",sans-serif;font-size:11px;text-transform:uppercase;display:block}
.ceo i{font-family:"Josefin Sans",sans-serif;font-style:normal;font-size:11px;color:var(--blue)}

/* services band */
.band{top:1590px;left:0;width:1200px;height:498px;background:linear-gradient(120deg,#1c44ad,#2148b2 60%,#1a3e9f)}
.band .eyebrow,.band .title,.band .body{color:#fff}
.band .title{font-size:31px;line-height:38px}
.call{font-family:"Josefin Sans",sans-serif;font-size:29px;font-weight:700;color:transparent;-webkit-text-stroke:1px #fff;text-transform:uppercase;white-space:nowrap}
.svc{position:absolute;width:208px;height:75px;border:1px solid rgba(255,255,255,.28);background:rgba(255,255,255,.05);color:#fff;font-family:"Josefin Sans",sans-serif;font-size:12.5px;line-height:21px;display:flex;align-items:center;justify-content:center;text-align:center}

/* team */
.card{position:absolute;top:2263px;width:203px;height:299px;background:#f4f4f5}
.card .photo{height:237px;background:linear-gradient(180deg,#eceef1 0%,#c9cfdb 55%,#2d58c9 100%)}
.card .name{height:62px;background:var(--blue);color:#fff;text-align:center;padding-top:12px}
.card .name b{font-family:"Josefin Sans",sans-serif;font-size:13px;display:block}
.card .name span{font-size:11px}
.arrow{position:absolute;z-index:2;top:2365px;width:37px;height:37px;background:#6c7078;display:flex;align-items:center;justify-content:center}

/* maintenance */
.maint{top:2694px;left:0;width:1200px;height:544px;background:var(--pale)}
.maint .photo{position:absolute;left:584px;top:0;width:616px;height:544px;background:linear-gradient(90deg,rgba(242,243,246,1) 0%,rgba(190,188,182,.6) 25%,#a8a49b 55%,#d8d3c8 100%)}
.ibtn{position:absolute;top:2954px;width:195px;height:53px;border:1px solid var(--blue);background:#fff;display:flex;align-items:center}
.ibtn .ic{width:51px;height:51px;background:var(--blue);display:flex;align-items:center;justify-content:center}
.ibtn span{flex:1;text-align:center;font-family:"Josefin Sans",sans-serif;font-size:13px;color:var(--blue)}

/* careers */
.acc{position:absolute;left:611px;width:427px;height:52px;background:#f4f4f5;border:1px solid var(--line);display:flex;align-items:center;padding:0 18px;font-family:"Josefin Sans",sans-serif;font-size:12px;color:#555;text-transform:uppercase}
.acc .plane{margin-right:9px}
.acc .pm{margin-left:auto;color:#aaa;font-size:16px}
.acc.open{background:var(--blue);color:#fff;border-color:var(--blue)}
.acc.open .pm{color:#fff}
.big-mark{top:3480px;left:160px;width:394px;height:208px;display:flex;align-items:center;gap:20px;font-family:"Josefin Sans",sans-serif;font-weight:700;font-size:40px;color:var(--blue);white-space:nowrap}
.big-mark .circ{width:160px;height:160px;border-radius:50%;border:6px solid var(--blue);flex-shrink:0}

/* footer */
.footer{top:3877px;left:0;width:1200px;height:372px;background:linear-gradient(120deg,#fafafb,#eef0f3)}
.fhead{font-family:"Josefin Sans",sans-serif;font-size:22px;color:#222}
.fline{width:34px;height:1px;background:var(--blue);margin-top:8px}
.flinks{list-style:none;margin-top:12px}
.flinks li{font-size:11px;height:31px;color:#333}
.news-in{position:absolute;left:836px;top:4067px;width:202px;height:30px;border:1px solid var(--line);background:#fff;font-size:9px;color:#999;padding:10px 10px}
.news-in .go{position:absolute;right:-1px;top:-1px;width:36px;height:30px;background:var(--blue);display:flex;align-items:center;justify-content:center}
.soc{width:27px;height:27px;background:#666a72;border-radius:3px}
.soc.b{background:var(--blue)}
.copybar{top:4249px;left:0;width:1200px;height:49px;background:var(--footer-bar);color:#fff;text-align:center;font-size:11.5px;padding-top:18px}
</style>
</head>
<body>

<!-- Top bar -->
<div class="abs topbar">
  <div class="contact">
    <span><svg width="11" height="11" viewBox="0 0 24 24"><path fill="#fff" d="M6.6 10.8a15 15 0 006.6 6.6l2.2-2.2c.3-.3.7-.4 1-.2 1.1.4 2.3.6 3.6.6.6 0 1 .4 1 1V20c0 .6-.4 1-1 1A17 17 0 013 4c0-.6.4-1 1-1h3.5c.6 0 1 .4 1 1 0 1.3.2 2.5.6 3.6.1.3 0 .7-.2 1z"/></svg>+1 555 018 42</span>
    <span style="opacity:.6">|</span>
    <span><svg width="11" height="9" viewBox="0 0 24 18"><path fill="#fff" d="M0 0h24v18H0z"/><path d="M2 2l10 7 10-7" stroke="#1f45aa" stroke-width="2" fill="none"/></svg>twaviation@support.com</span>
  </div>
</div>

<!-- Navigation -->
<header class="abs nav">
  <div class="brand"><span class="dot"></span>TW Aviation</div>
  <nav class="menu">
    <a class="active">Home</a><a>About Us</a><a>Aircraft Maintenance</a><a>Aircraft Cleaning</a><a>Careers</a><a>Contact</a>
  </nav>
</header>

<!-- Hero -->
<section class="abs hero" role="img" aria-label="Black and white photo of a helicopter on a helipad with mechanics working beside it under a cloudy sky">
  <div class="shade"></div>
  <div class="hero-text">
    <div class="eyebrow-light">Welcome to TW Aviation</div>
    <h1>TW Aviation is insured and all of our<br>mechanics are licensed by the NQB with an<br>Airframe &amp; Powerplant rating</h1>
  </div>
  <a class="btn">Get Started</a>
</section>

<!-- Booking -->
<section class="abs booking">
  <div class="label"><small>Book your service</small><strong>ONLINE</strong></div>
  <div class="field" style="left:314px;top:45px">Lorem Ipsum</div>
  <div class="field" style="left:492px;top:45px">Type Of Service</div>
  <div class="field" style="left:671px;top:45px">Lorem Ipsum</div>
  <div class="field" style="left:314px;top:104px">Lorem Ipsum</div>
  <div class="field" style="left:492px;top:104px">Lorem Ipsum</div>
  <div class="submit" style="left:671px;top:104px">Submit Booking</div>
</section>

<!-- About -->
<div class="abs about-media" role="img" aria-label="Mechanic in a cap checking a tablet beside a helicopter in a hangar">
  <div class="play"><svg width="20" height="22" viewBox="0 0 20 22"><path d="M2 1l17 10L2 21z" fill="#1f45aa"/></svg></div>
</div>
<div class="abs eyebrow" style="top:1056px;left:611px">About Us</div>
<h2 class="abs title" style="top:1070px;left:609px">TW Aviation Introduction</h2>
<p class="abs body" style="top:1122px;left:611px;width:430px">TW Aviation Services is a company with aircraft maintenance experience. We focus on inspections of aircraft . Our Aircraft Mechanics who are pilots and IA's have experience many aircraft but specialize in the Kestrane KT420 , KT425 KT435, The Belvanko T82 and Morvell Tarrant 512 .</p>
<div class="abs quote">"Get in your aircraft and fly knowing you have the best maintenance crew in the business!"</div>
<p class="abs body" style="top:1322px;left:611px;width:430px">Our focus is safety and maintain aircraft day in and day out so our customer can operate the aircraft safely while keeping up with all the manufacturers inspections. We know aircraft maintenance &amp; maintenance planning . Leave the technical and tedious things to us.</p>
<div class="abs divider" style="top:1430px;left:611px;width:427px"></div>
<div class="abs ceo">
  <div class="avatar" role="img" aria-label="Portrait of the CEO"></div>
  <div><b>Mateus Ferreira</b><i>CEO – Founder</i></div>
</div>
<div class="abs" style="top:1466px;left:812px;width:76px;height:32px;background:#f3f3f4" role="img" aria-label="CEO signature"></div>
<a class="abs btn" style="top:1460px;left:908px;width:130px;height:47px">Learn More</a>

<!-- What we do -->
<section class="abs band">
  <div class="abs eyebrow" style="top:84px;left:160px">What we do?</div>
  <h2 class="abs title" style="top:100px;left:160px">We're a mobile AOG team<br>who is available 24/7</h2>
  <p class="abs body" style="top:187px;left:160px;width:410px">Lorem ipsum dolor sit amet, consectetur adipiscing elit, sed do dunt ut labore et dolore magna aliqua. Ut enim ad minim veniam, quis nostrud exercitation ullamco est laboris nisi ut aliquip ex ea commodo nord vor consequat. Duis aute il irure dolor in reprehenderit in voluptate velit esse cillum dolor. Et harum quidem rerum facilis est et expedita tinctio. Nam libero tempore, cum soluta nobis est eligendi optio cumque nihil.</p>
  <div class="abs divider" style="top:354px;left:160px;width:407px;background:rgba(255,255,255,.3)"></div>
  <div class="abs call" style="top:386px;left:160px">Call us now at +1 555 0199</div>
  <div class="svc" style="left:611px;top:82px">Scheduled &amp; Unscheduled<br>aircraft maintenance</div>
  <div class="svc" style="left:831px;top:82px">Major &amp; Minor repairs</div>
  <div class="svc" style="left:611px;top:169px">STC installations</div>
  <div class="svc" style="left:831px;top:169px">Aircraft Weight &amp; Balance</div>
  <div class="svc" style="left:611px;top:256px">Aircraft Painting</div>
  <div class="svc" style="left:831px;top:256px">Aircraft Cleaning</div>
  <div class="svc" style="left:611px;top:341px">Maintenance Tracking Utilizing<br>Tracking Programs</div>
  <div class="svc" style="left:831px;top:341px">Removal &amp; Installation<br>of Components</div>
</section>

<!-- Staff -->
<div class="abs eyebrow" style="top:2170px;left:0;width:1200px;text-align:center">Team Members</div>
<h2 class="abs title" style="top:2182px;left:0;width:1200px;text-align:center">Meet The Staff</h2>
<div class="card" style="left:162px"><div class="photo" role="img" aria-label="Engineer in blue overalls holding a wrench"></div><div class="name"><b>Dorian Vask</b><span>(Aircraft Engineer)</span></div></div>
<div class="card" style="left:386px"><div class="photo" role="img" aria-label="Engineer in blue overalls with arms crossed"></div><div class="name"><b>Colin Ardent</b><span>(Aircraft Engineer)</span></div></div>
<div class="card" style="left:611px"><div class="photo" role="img" aria-label="Smiling engineer in blue overalls"></div><div class="name"><b>Nolan Pryce</b><span>(Aircraft Engineer)</span></div></div>
<div class="card" style="left:836px"><div class="photo" role="img" aria-label="Bearded engineer in a blue cap and overalls"></div><div class="name"><b>Tobias Wrenn</b><span>(Aircraft Engineer)</span></div></div>
<div class="arrow" style="left:143px"><svg width="14" height="10" viewBox="0 0 14 10"><path d="M13 5H1M5 1L1 5l4 4" stroke="#fff" fill="none"/></svg></div>
<div class="arrow" style="left:1018px"><svg width="14" height="10" viewBox="0 0 14 10"><path d="M1 5h12M9 1l4 4-4 4" stroke="#fff" fill="none"/></svg></div>
<a class="abs sans" style="top:2599px;left:0;width:1200px;text-align:center;font-size:12px;color:#555;text-decoration:underline">click here to view all members</a>

<!-- Aircraft Maintenance -->
<section class="abs maint">
  <div class="photo" role="img" aria-label="Mechanics working on a helicopter rotor head and engine"></div>
  <div class="abs eyebrow" style="top:82px;left:160px">Service Details</div>
  <h2 class="abs title" style="top:96px;left:160px">Aircraft Maintenance</h2>
  <p class="abs body" style="top:148px;left:160px;width:430px">Lorem ipsum dolor sit amet, consectetur adipiscing elit, sed do mod tempor incididunt ut labore et dolore magna aliqua. Ut enim ad minis emalit veniam, quis nostrud exercitation ullamco laboris nisi ut aliquip ex ea commodo consequat.</p>
  <p class="abs body" style="top:334px;left:160px;width:430px">Nemo enim ipsam voluptatem quia voluptas sit aspernatur aut odit aut fugit, sed quia consequuntur magni dolores eos qui ratione voluptatem</p>
  <a class="abs btn" style="top:414px;left:160px;width:134px;height:47px">Get Service</a>
</section>
<div class="ibtn" style="left:160px"><div class="ic"><svg width="24" height="24" viewBox="0 0 24 24"><circle cx="12" cy="12" r="8" stroke="#fff" stroke-width="2" fill="none" stroke-dasharray="4 2"/><circle cx="12" cy="12" r="3" fill="#fff"/></svg></div><span>Lorem Ipsum</span></div>
<div class="ibtn" style="left:382px"><div class="ic"><svg width="24" height="24" viewBox="0 0 24 24"><circle cx="12" cy="12" r="9" stroke="#fff" stroke-width="2" fill="none"/><circle cx="12" cy="12" r="4" stroke="#fff" fill="none"/></svg></div><span>Lorem Ipsum</span></div>

<!-- Careers -->
<div class="abs eyebrow" style="top:3320px;left:0;width:1200px;text-align:center">Our Approach</div>
<h2 class="abs title" style="top:3332px;left:0;width:1200px;text-align:center">Careers</h2>
<p class="abs body" style="top:3400px;left:160px;width:430px">Are you are passionate about helping clients in aviation and aerospace succeed? Interested in working with a diverse team of industry experts? Elevate your career with TW Aviation.</p>
<div class="abs big-mark"><span class="circ"></span>TW Aviation</div>
<p class="abs body" style="top:3714px;left:160px;width:420px">Lorem ipsum dolor sit amet, consectetur adipiscing elit, sed do eius-mod tempor incididunt ut labore et dolore magna aliqua.</p>
<a class="abs sans" style="top:3785px;left:160px;font-size:10px;color:var(--blue);text-transform:uppercase">Explore Careers &nbsp;⟶</a>
<div class="acc" style="top:3406px"><svg class="plane" width="16" height="10" viewBox="0 0 16 10"><path d="M0 5h16M9 0l-2 5 2 5M2 2v6" stroke="#1f45aa" stroke-width="1.6" fill="none"/></svg>Aircraft Dispatcher<span class="pm">+</span></div>
<div class="acc" style="top:3473px"><svg class="plane" width="16" height="10" viewBox="0 0 16 10"><path d="M0 5h16M9 0l-2 5 2 5M2 2v6" stroke="#1f45aa" stroke-width="1.6" fill="none"/></svg>Aircraft Engineer<span class="pm">+</span></div>
<div class="acc open" style="top:3540px"><svg class="plane" width="16" height="10" viewBox="0 0 16 10"><path d="M0 5h16M9 0l-2 5 2 5M2 2v6" stroke="#fff" stroke-width="1.6" fill="none"/></svg>Aircraft Mechanic<span class="pm">—</span></div>
<div class="acc" style="top:3607px"><svg class="plane" width="16" height="10" viewBox="0 0 16 10"><path d="M0 5h16M9 0l-2 5 2 5M2 2v6" stroke="#1f45aa" stroke-width="1.6" fill="none"/></svg>Aircraft Technician<span class="pm">+</span></div>
<div class="acc" style="top:3675px"><svg class="plane" width="16" height="10" viewBox="0 0 16 10"><path d="M0 5h16M9 0l-2 5 2 5M2 2v6" stroke="#1f45aa" stroke-width="1.6" fill="none"/></svg>Aircraft Dispatcher<span class="pm">+</span></div>
<div class="acc" style="top:3742px"><svg class="plane" width="16" height="10" viewBox="0 0 16 10"><path d="M0 5h16M9 0l-2 5 2 5M2 2v6" stroke="#1f45aa" stroke-width="1.6" fill="none"/></svg>Aircraft Pilot<span class="pm">+</span></div>

<!-- Footer -->
<footer class="abs footer">
  <div class="brand abs" style="top:78px;left:160px;font-size:26px"><span class="dot"></span>TW Aviation</div>
  <p class="abs" style="top:158px;left:160px;width:210px;font-size:10.5px;line-height:22px;color:#444">Flannel selfies authentic literally man bun hella thundercats kombucha letist forage of lorem ipsum dolor.</p>
  <div class="abs divider" style="top:237px;left:160px;width:205px"></div>
  <div class="abs" style="top:258px;left:160px;font-size:11px;color:#333;display:flex;gap:12px;align-items:center"><svg width="10" height="10" viewBox="0 0 24 24"><path fill="#1f45aa" d="M6.6 10.8a15 15 0 006.6 6.6l2.2-2.2c.3-.3.7-.4 1-.2 1.1.4 2.3.6 3.6.6.6 0 1 .4 1 1V20c0 .6-.4 1-1 1A17 17 0 013 4c0-.6.4-1 1-1h3.5c.6 0 1 .4 1 1 0 1.3.2 2.5.6 3.6.1.3 0 .7-.2 1z"/></svg>555 010 372</div>
  <div class="abs" style="top:285px;left:160px;font-size:11px;color:#333;display:flex;gap:12px;align-items:center"><svg width="10" height="8" viewBox="0 0 24 18"><path fill="#1f45aa" d="M0 0h24v18H0z"/></svg>twaviation@support.com</div>

  <div class="abs" style="top:72px;left:437px"><div class="fhead">Quick Links</div><div class="fline"></div>
    <ul class="flinks"><li>Home</li><li>About Us</li><li>Aircraft Maintenance</li><li>Aircraft Cleaning</li><li>Careers</li><li>Contact</li></ul></div>
  <div class="abs" style="top:72px;left:653px"><div class="fhead">Information</div><div class="fline"></div>
    <ul class="flinks"><li>Sitemap</li><li>Terms Of Use</li><li>Privacy Policy</li><li>Booking Services</li><li>Text Filler</li><li>Another Text Filler</li></ul></div>
  <div class="abs" style="top:70px;left:836px;width:205px"><div class="fhead">Newsletter</div><div class="fline"></div>
    <p style="margin-top:12px;font-size:10px;line-height:20px;color:#444">Subscribe to our newsletter to get notified with all of the news, updates</p></div>
  <div class="abs" style="top:268px;left:836px;display:flex;align-items:center;gap:10px;font-size:10px;color:#444">Find Us Also At:
    <span class="soc" style="margin-left:8px"></span><span class="soc b"></span><span class="soc"></span></div>
</footer>
<div class="news-in">Your E-mail Address<span class="go"><svg width="13" height="13" viewBox="0 0 24 24"><path d="M2 11L22 2l-9 20-2-9z" stroke="#fff" stroke-width="2" fill="none"/></svg></span></div>
<div class="abs copybar">Copyright © 2020 <b>TW Aviation</b> - All Rights Reserved</div>

</body>
</html>
```